Best in class business looking for best in class stationery that accurately reflects the brand image we are trying to build as the brand expands throughout the country. The Varying items should be an eye catching design that makes even the simplest letter or small business card stand out in the crowd.

Target Market(s)

Professionals

Industry/Entity Type

Real Estate

Other font styles liked:
• See atttached logo

Requirements
Must have
• Letterhead
• Business cards
• Envelopes
• Labels for larger mailings
Nice to have
• Folders
• Notebook
Should not have
• Stale design elements

```html
<!DOCTYPE html>
<html lang="en">
<head>
<meta charset="utf-8">
<title>Ridgeline Property Group – Business Cards</title>
<link href="https://fonts.googleapis.com/css2?family=Cinzel:wght@500&family=Arimo:wght@400&display=swap" rel="stylesheet">
<style>
  :root {
    --backdrop: #3a322e;
    --card: #141517;
    --card-edge: #0b0b0c;
    --silver: #9a9ca1;
    --silver-soft: #7d7f84;
    --royal: #3346a8;
    --royal-light: #3f55c4;
    --ink-light: #f2f2f2;
    --divider: #8d8f94;
  }
  * { margin: 0; padding: 0; box-sizing: border-box; }
  html, body { width: 1200px; height: 864px; overflow: hidden; }
  body {
    background: var(--backdrop);
    position: relative;
    font-family: "Arimo", Arial, sans-serif;
  }
  .card {
    position: absolute;
    width: 520px;
    height: 298px;
    background: var(--card);
    border-radius: 3px;
    box-shadow: 0 14px 30px rgba(0,0,0,.45), 0 2px 0 var(--card-edge);
  }
  .card--front { left: 80px; top: 90px; }
  .card--back { left: 600px; top: 476px; }

  /* Front */
  .brand {
    position: absolute;
    display: flex;
    align-items: center;
    gap: 10px;
    font-family: "Cinzel", Georgia, serif;
    font-weight: 500;
    white-space: nowrap;
  }
  .brand__mark { width: 12px; height: 12px; flex: none; }
  .card--front .brand {
    left: 0; right: 0; top: 104px;
    justify-content: center;
    font-size: 24px;
    color: var(--silver);
    letter-spacing: 1px;
  }
  .card--front .brand__mark { background: var(--silver); }
  .front-rule {
    position: absolute; left: 80px; right: 80px; top: 150px;
    height: 1px; background: var(--silver-soft);
  }
  .front-web {
    position: absolute; left: 0; right: 0; top: 180px;
    text-align: center;
    font-size: 14px;
    letter-spacing: 5px;
    color: var(--silver-soft);
  }

  /* Back */
  .card--back .brand {
    left: 20px; width: 290px; top: 118px;
    justify-content: center;
    font-size: 17px;
    color: var(--royal);
  }
  .card--back .brand__mark { background: var(--royal); }
  .back-rule {
    position: absolute; left: 30px; width: 270px; top: 154px;
    height: 1px; background: var(--royal);
  }
  .divider {
    position: absolute; left: 322px; top: 40px; bottom: 40px;
    width: 1px;
    background: linear-gradient(var(--card), var(--divider) 30%, var(--divider) 70%, var(--card));
  }
  .contact {
    position: absolute; left: 342px; top: 44px; right: 16px;
    color: var(--ink-light);
    font-size: 13px;
    line-height: 1.35;
  }
  .contact__name { color: var(--royal-light); font-size: 17px; line-height: 1.1; }
  .contact__role { color: var(--royal-light); font-size: 13px; margin-bottom: 10px; }
  .contact__address { margin-bottom: 6px; }
  .contact__list { list-style: none; }
  .contact__item { display: flex; align-items: center; gap: 8px; height: 19px; }
  .contact__icon { width: 11px; height: 11px; flex: none; fill: var(--ink-light); }
</style>
</head>
<body>
  <section class="card card--front" aria-label="Business card front">
    <div class="brand"><span class="brand__mark"></span>Ridgeline Property Group</div>
    <div class="front-rule"></div>
    <p class="front-web">www.example.com</p>
  </section>

  <section class="card card--back" aria-label="Business card back">
    <div class="brand"><span class="brand__mark"></span>Ridgeline Property Group</div>
    <div class="back-rule"></div>
    <div class="divider"></div>
    <div class="contact">
      <p class="contact__name">Mark Ellison</p>
      <p class="contact__role">President</p>
      <p class="contact__address">2170 Alder Crest Lane<br>Lakeview, NY 11020</p>
      <ul class="contact__list">
        <li class="contact__item">
          <svg class="contact__icon" viewBox="0 0 12 12"><path d="M1 4c0-2 2-3 5-3s5 1 5 3v1H8V3.5H4V5H1zM2 6h8l1 5H1z"/></svg>555 0142 2253
        </li>
        <li class="contact__item">
          <svg class="contact__icon" viewBox="0 0 12 12"><path d="M3 0h6v12H3zM4 1.5v8h4v-8z"/></svg>555 0187 5335
        </li>
        <li class="contact__item">
          <svg class="contact__icon" viewBox="0 0 12 12"><path d="M3 0h5v4H3zM1 5h10v6H1zM3 7v1h6V7z"/></svg>555 0163 3856
        </li>
        <li class="contact__item">
          <svg class="contact__icon" viewBox="0 0 12 12"><path d="M0 2h12v8H0zM1 3l5 4 5-4v-.2H1z"/></svg>mark@example.com
        </li>
        <li class="contact__item">
          <svg class="contact__icon" viewBox="0 0 12 12"><circle cx="6" cy="6" r="5.5"/><path d="M6 1v10M1 6h10" stroke="#141517" stroke-width="1" fill="none"/></svg>www.example.com
        </li>
      </ul>
    </div>
  </section>
</body>
</html>
```